Form With Tamsin - Health and Wellness Business Card and Logo

I need a business card design with a logo for my business you can check out at www.formwithtamsin.net. I want something more original, simplistic, and memorable than the basic logo I have on my site currently. I am a health and wellness coach and I offer mindset coaching and nutrition plans. I like the colour teal and dark grey/black for my theme colours. I emphasize growth, longterm change, and the whole package of "healthy mind, healthy body, healthy life". I had played around the idea of intertwining 3 T's or incorporating growth (leaves etc.) into my design. I want my expertise and experience to show through. In one glance I want people to understand with confidence I can help them accomplish anything they set their minds to. I look forward to seeing what everyone comes up with!

Industry/Entity Type

Health And Wellness

Contact Information for Business Card

Form With Tamsin
Tamsin Arlow
BSc, Health & Wellness Coach
"Manifest your best"
www.formwithtamsin.net
formwithtamsin@mailo.example
613-472-9186
[Instagram logo] @tamsinarlow

Colors
33b8a4
ffffff
333333
000000

Requirements
Must have
• A memorable and unique logo for my business!
Nice to have
• Could have the phrase "Are you unhappy with your body and state of health?" or "It takes the right skills to develop habits in order to create long term change. I can help you get there."

```html
<!DOCTYPE html>
<html lang="en">
<head>
<meta charset="utf-8">
<title>Form With Tamsin – Business Card</title>
<link rel="stylesheet" href="https://fonts.googleapis.com/css2?family=Questrial&family=Open+Sans:wght@400;700&display=swap">
<style>
  :root {
    --backdrop: #2a2a2a;
    --card: #ffffff;
    --teal: #1f8a82;
    --ink: #222222;
    --ink-soft: #555555;
    --rule: #9a9a9a;
  }
  * { box-sizing: border-box; margin: 0; padding: 0; }
  html, body { width: 1200px; height: 1000px; overflow: hidden; }
  body { background: var(--backdrop); position: relative; font-family: "Open Sans", sans-serif; }

  .card {
    position: absolute;
    left: 250px;
    width: 700px;
    height: 400px;
    background: var(--card);
    box-shadow: 0 10px 30px rgba(0,0,0,0.45);
    overflow: hidden;
  }
  .card--front { top: 60px; }
  .card--back  { top: 530px; }

  /* Front */
  .brand-lockup {
    position: absolute;
    left: 0; right: 0; top: 140px;
    display: flex; flex-direction: column; align-items: center;
  }
  .brand-lockup__mark {
    display: flex; align-items: center; gap: 12px;
    color: var(--teal);
    font-family: "Questrial", sans-serif;
    font-size: 40px;
    line-height: 1;
  }
  .brand-lockup__square { width: 34px; height: 34px; background: var(--teal); }
  .brand-lockup__rule { width: 270px; height: 2px; background: var(--rule); margin: 14px 0 8px; }
  .brand-lockup__name {
    font-family: "Questrial", sans-serif;
    font-size: 30px;
    color: var(--ink);
    letter-spacing: 0.5px;
  }

  /* Back */
  .wordmark {
    position: absolute; left: 60px; top: 40px;
    font-family: "Questrial", sans-serif;
    font-size: 46px;
    color: var(--ink);
    letter-spacing: 1px;
  }
  .name-tab { position: absolute; left: 0; top: 132px; width: 14px; height: 46px; background: var(--teal); }
  .person { position: absolute; left: 40px; top: 126px; }
  .person__name { font-weight: 700; font-size: 25px; color: var(--teal); letter-spacing: 0.5px; }
  .person__role { font-weight: 700; font-size: 18px; color: var(--ink-soft); margin-top: -2px; }

  .contact { position: absolute; left: 40px; top: 214px; list-style: none; color: var(--ink-soft); font-size: 17px; line-height: 28px; }
  .contact__tagline { font-style: italic; margin-bottom: 6px; }
  .contact__item { display: flex; align-items: center; gap: 12px; }
  .contact__icon { width: 14px; height: 14px; fill: var(--teal); flex: none; }
  .contact__web-accent { color: var(--teal); }

  .corner-mark {
    position: absolute; right: 40px; bottom: 40px;
    display: flex; align-items: center; gap: 10px;
    color: var(--teal);
    font-family: "Questrial", sans-serif;
    font-size: 26px;
  }
  .corner-mark__square { width: 26px; height: 26px; background: var(--teal); }
</style>
</head>
<body>

<section class="card card--front" aria-label="Card front">
  <div class="brand-lockup">
    <div class="brand-lockup__mark">
      <span class="brand-lockup__square"></span>
      <span>Form With Tamsin</span>
    </div>
    <div class="brand-lockup__rule"></div>
    <div class="brand-lockup__name">form with tamsin</div>
  </div>
</section>

<section class="card card--back" aria-label="Card back">
  <div class="wordmark">form with tamsin</div>
  <div class="name-tab"></div>
  <div class="person">
    <div class="person__name">TAMSIN ARLOW</div>
    <div class="person__role">BSc, Health &amp; Wellness Coach</div>
  </div>
  <ul class="contact">
    <li class="contact__tagline">"Manifest your best"</li>
    <li class="contact__item">
      <svg class="contact__icon" viewBox="0 0 16 16" aria-hidden="true"><path d="M3.6 1.2l2.2 2.6-1.3 1.8c.9 2 2.4 3.5 4.3 4.3l1.8-1.3 2.6 2.2-1.4 2.4C6.7 12.8 3.2 9.3 1.2 3.2z"/></svg>
      <span>613-472-9186</span>
    </li>
    <li class="contact__item">
      <svg class="contact__icon" viewBox="0 0 16 16" aria-hidden="true"><path d="M1 3h14v10H1z M2 4.2v.6l6 4 6-4v-.6z" fill-rule="evenodd"/></svg>
      <span>formwithtamsin@mailo.example</span>
    </li>
    <li class="contact__item">
      <svg class="contact__icon" viewBox="0 0 16 16" aria-hidden="true"><circle cx="8" cy="8" r="7"/><path d="M1 8h14M8 1v14" stroke="#fff" stroke-width="1"/></svg>
      <span>www.<span class="contact__web-accent">formwithtamsin</span>.net</span>
    </li>
    <li class="contact__item">
      <svg class="contact__icon" viewBox="0 0 16 16" aria-hidden="true"><circle cx="8" cy="8" r="6"/></svg>
      <span>@tamsinarlow</span>
    </li>
  </ul>
  <div class="corner-mark">
    <span class="corner-mark__square"></span>
    <span>Form With Tamsin</span>
  </div>
</section>

</body>
</html>
```